Law Firm Stationery Design Project

This is the final part of a law firm rebrand project. The logo design is near completion, and I am also asking for business card designs in a separate contest. I will post the winning logo design to this project sometime tomorrow.

The job here is to design letterhead, business envelopes, shipping labels, memorandum, report, and the like, based on the following criteria (mainly quoted from the business card project):

My firm specializes in representing startup companies. This means I routinely interact with young entrepreneurs and the (typically) older, more experienced investors who fund them. I need to appeal to the former without offending the latter. I'm interesting in conveying the idea that my firm is a credible alternative to larger, brand-name firms. I use these words in positioning my firm in this market: creative; flexible; fair; practical; experienced. The winning design needs to convey this idea.

I'm will also be re-working my website soon and will likely use noto sans and noto serif as my primary website fonts. I'd like the stationary (just as I have asked the same of the business card) to use a font that is similar, but also compatible with the font used in the firm's logo.

Target Market(s)

Young entrepreneurs and older investors who collaborate in the formation and funding of high-tech startup companies located in the Pacific Northwest.

Industry/Entity Type

Law Firm

Font styles to use
Serif
Sans Serif

Requirements
Must have
• - Firm logo, firm tag line, return mailing address, firm website url, firm phone number, attorney name, attorney title, attorney email address, and attorney twitter account. I will provide the specific contact information to the winning designer; you may use fictional data in preparing your design.

The attached pdf for a proposed business card indicates the kind of tone that I have in mind, recognizing that it is my amateur attempt at doing what I'm hoping the winning designer is able to do so much better.

```html
<!DOCTYPE html>
<html lang="en">
<head>
<meta charset="utf-8">
<title>Harwell Law PLLC — Stationery</title>
<link rel="stylesheet" href="https://fonts.googleapis.com/css2?family=Montserrat:wght@400;500&family=Noto+Sans:wght@400;500&display=swap">
<style>
  :root{
    --bg:#e9eaec;
    --paper:#fbfbfb;
    --paper-edge:#d9dbde;
    --navy:#2d5785;
    --navy-deep:#1f4a7a;
    --ink:#6b7078;
    --rule:#c7cbd1;
    --white:#ffffff;
  }
  *{box-sizing:border-box;margin:0;padding:0}
  html,body{width:1200px;height:864px;overflow:hidden;background:var(--bg)}
  body{position:relative;font-family:"Noto Sans",Arial,sans-serif;color:var(--ink)}

  .sheet{position:absolute;background:var(--paper);box-shadow:0 1px 0 var(--paper-edge),0 6px 18px rgba(0,0,0,.08)}

  /* wordmark: one font, one weight, one colour + a plain square */
  .wordmark{display:flex;align-items:center;gap:8px;font-family:"Montserrat",Arial,sans-serif;font-weight:500;color:var(--navy);letter-spacing:.08em;white-space:nowrap}
  .wordmark .mark{display:block;border:2px solid currentColor;flex:none}
  .tagline{font-family:"Noto Sans",Arial,sans-serif;font-weight:500;color:var(--navy);letter-spacing:.16em;text-transform:uppercase;white-space:nowrap}

  /* letterhead */
  .letterhead{left:40px;top:40px;width:340px;height:440px}
  .letterhead .head{position:absolute;top:30px;left:0;right:0;display:flex;flex-direction:column;align-items:center;gap:5px}
  .letterhead .wordmark{font-size:13px}
  .letterhead .wordmark .mark{width:11px;height:11px;border-width:1.5px}
  .letterhead .tagline{font-size:5.5px}
  .letterhead .footer{position:absolute;left:30px;right:30px;bottom:26px;border-top:1px solid var(--rule);padding-top:6px;font-size:6px;letter-spacing:.05em;display:flex;justify-content:space-between}

  /* presentation folder */
  .folder{left:410px;top:40px;width:340px;height:440px}
  .folder .spine{position:absolute;left:14px;top:0;bottom:0;width:10px;border-left:1px solid var(--rule);border-right:1px solid var(--rule)}
  .folder .head{position:absolute;top:96px;right:34px;display:flex;flex-direction:column;align-items:flex-end;gap:7px}
  .folder .wordmark{font-size:17px;gap:10px}
  .folder .wordmark .mark{width:16px;height:16px}
  .folder .tagline{font-size:6.5px}
  .folder .url{position:absolute;left:0;right:0;bottom:30px;text-align:center;font-size:7px;letter-spacing:.08em}

  /* business cards */
  .card{position:absolute;width:300px;height:171px}
  .card-front{left:810px;top:40px;background:var(--white)}
  .card-front .brand{position:absolute;left:20px;top:32px;display:flex;flex-direction:column;gap:5px}
  .card-front .wordmark{font-size:11px;gap:6px}
  .card-front .wordmark .mark{width:9px;height:9px;border-width:1.5px}
  .card-front .tagline{font-size:4.5px;letter-spacing:.12em}
  .card-front .contact{position:absolute;left:182px;top:28px;font-size:7px;line-height:1.6}
  .card-front .contact .name{font-family:"Montserrat",Arial,sans-serif;font-weight:500;font-size:8.5px;color:var(--navy);letter-spacing:.06em;text-transform:uppercase}
  .card-front .contact .title{margin-bottom:8px}
  .card-back{left:810px;top:230px;background:var(--navy-deep);box-shadow:0 6px 18px rgba(0,0,0,.12)}
  .card-back .wordmark{position:absolute;left:0;right:0;top:40px;justify-content:center;font-size:14px;color:var(--white)}
  .card-back .wordmark .mark{width:12px;height:12px;border-width:1.5px}
  .card-back .tagline{position:absolute;left:0;right:0;top:62px;text-align:center;font-size:5.5px;color:var(--white);opacity:.85}
  .card-back .services{position:absolute;left:26px;right:26px;bottom:30px;text-align:center;font-size:6.5px;line-height:1.7;color:var(--white);opacity:.8;letter-spacing:.04em}

  /* envelopes */
  .envelope{top:520px;width:540px;height:235px}
  .envelope-front{left:40px}
  .envelope-front .wordmark{position:absolute;left:26px;top:24px;font-size:14px}
  .envelope-front .wordmark .mark{width:12px;height:12px;border-width:1.5px}
  .envelope-front .tagline{position:absolute;left:26px;top:45px;font-size:5.5px}
  .envelope-front .return{position:absolute;left:26px;top:60px;font-size:6px;letter-spacing:.05em}
  .envelope-back{left:610px}
  .envelope-back svg{position:absolute;inset:0}
</style>
</head>
<body>

  <section class="sheet letterhead" aria-label="Letterhead">
    <header class="head">
      <div class="wordmark"><span class="mark"></span>HARWELL LAW PLLC</div>
      <div class="tagline">Practical counsel for bold ventures</div>
    </header>
    <footer class="footer">
      <span>1207 Harbor Avenue, Tacoma, WA 98402</span>
      <span>Tel 253.555.0148</span>
      <span>www.harwelllawpllc.com</span>
    </footer>
  </section>

  <section class="sheet folder" aria-label="Presentation folder">
    <div class="spine"></div>
    <header class="head">
      <div class="wordmark"><span class="mark"></span>HARWELL LAW PLLC</div>
      <div class="tagline">Practical counsel for bold ventures</div>
    </header>
    <div class="url">www.harwelllawpllc.com</div>
  </section>

  <section class="sheet card card-front" aria-label="Business card front">
    <div class="brand">
      <div class="wordmark"><span class="mark"></span>HARWELL LAW</div>
      <div class="tagline">Practical counsel for bold ventures</div>
    </div>
    <div class="contact">
      <div class="name">Noah R. Harwell</div>
      <div class="title">Attorney at Law</div>
      <div>253.555.0148</div>
      <div>noah@harwelllawpllc.com</div>
      <div>@noahharwell</div>
      <div>harwelllawpllc.com</div>
    </div>
  </section>

  <section class="card card-back" aria-label="Business card back">
    <div class="wordmark"><span class="mark"></span>HARWELL LAW</div>
    <div class="tagline">Practical counsel for bold ventures</div>
    <div class="services">Startup Formation · Venture Financing<br>Contracts · Mergers &amp; Acquisitions</div>
  </section>

  <section class="sheet envelope envelope-front" aria-label="Envelope front">
    <div class="wordmark"><span class="mark"></span>HARWELL LAW PLLC</div>
    <div class="tagline">Practical counsel for bold ventures</div>
    <div class="return">1207 Harbor Avenue, Tacoma, WA 98402</div>
  </section>

  <section class="sheet envelope envelope-back" aria-label="Envelope back">
    <svg width="540" height="235" viewBox="0 0 540 235">
      <path d="M0 0 L0 70 L20 78 L520 78 L540 70 L540 0" fill="none" stroke="var(--rule)" stroke-width="1"/>
      <line x1="0" y1="0" x2="540" y2="0" stroke="var(--rule)"/>
    </svg>
  </section>

</body>
</html>
```